TownDailyo - Business card + Stationery
"Discover fresh corners of your town, daily!" "Today's leading daily deals +"
TownDailyo - Business card + Stationery - Information Technology
Creative Brief
Use specific fonts
Font used is good but open to new ideas
Bright & Fun-filled
Marcus Delwyn
Creator + Director
marcus@towndailyo.example
towndailyo.example
I am looking for a modern catchy design for a new set of business cards. Looking for stationery such as: email template - small logo with web link - Post card - Note pad etc... Looking for a modern design that contains the web link and text to match business card theme. Open to new ideas. Chatterbook and Chirplet logo "TOWNDAILYO" can be used on the cards too. I will make further comments as the various designs come in.
Logo + www. << >>.com on either side of the logo Text at bottom Discover fresh corners of your town, daily

```html
<!DOCTYPE html>
<html lang="en">
<head>
<meta charset="utf-8">
<title>TownDailyo – Business Card Options</title>
<link href="https://fonts.googleapis.com/css2?family=Open+Sans:wght@400;600;700;800&family=Cinzel:wght@400;600&display=swap" rel="stylesheet">
<style>
  :root{
    --sheet:#e9e4dc;
    --brand-blue:#1f7fcf;
    --brand-blue-light:#4aa3e3;
    --brand-blue-pale:#cfe6f7;
    --card-white:#ffffff;
    --ink-dark:#3a3a3a;
    --label-ink:#2f2f2f;
    --shadow:rgba(0,0,0,.22);
  }
  *{margin:0;padding:0;box-sizing:border-box}
  html,body{width:1200px;height:821px;overflow:hidden}
  body{background:var(--sheet);font-family:"Open Sans",Arial,sans-serif;position:relative}

  .card{position:absolute;width:516px;border-radius:18px;overflow:hidden;box-shadow:0 4px 10px var(--shadow)}
  .card--front{height:372px;top:24px}
  .card--back{height:300px;top:492px}
  .card--a{left:65px}
  .card--b{left:619px}
  .card svg.card-bg{position:absolute;inset:0;width:100%;height:100%}

  .skyline{position:absolute;right:70px;top:150px;width:150px;height:170px;border-radius:2px}
  .card--a .skyline{background:linear-gradient(180deg,rgba(255,255,255,.10),rgba(255,255,255,.02))}
  .card--b .skyline{background:linear-gradient(180deg,rgba(31,127,207,.12),rgba(31,127,207,.03))}

  .brand{position:absolute;display:flex;align-items:center;gap:8px;font-weight:800;letter-spacing:.5px;white-space:nowrap}
  .brand-mark{width:14px;height:14px;flex:none}
  .brand--front{left:34px;top:40px;font-size:30px;color:var(--brand-blue)}
  .brand--front .brand-mark{background:var(--brand-blue)}
  .brand--back{left:0;right:0;top:108px;justify-content:center;font-size:42px}
  .card--a .brand--back{color:var(--card-white)}
  .card--a .brand--back .brand-mark{background:var(--card-white)}
  .card--b .brand--back{color:var(--brand-blue)}
  .card--b .brand--back .brand-mark{background:var(--brand-blue)}
  .brand-mark.size-lg{width:20px;height:20px}

  .contacts{position:absolute;left:30px;top:208px;list-style:none;font-size:11.5px;line-height:20px}
  .contacts li{display:flex;align-items:center;gap:8px}
  .contacts .icon{width:11px;height:11px;flex:none}
  .card--a .contacts{color:var(--card-white)}
  .card--b .contacts{color:var(--ink-dark)}
  .social-box{display:inline-block;width:10px;height:10px;border-radius:2px}
  .card--a .social-box{background:var(--card-white)}
  .card--b .social-box{background:var(--brand-blue)}

  .person{position:absolute;right:26px;top:300px;text-align:right;line-height:17px}
  .person-name{font-weight:700;font-size:14px}
  .person-role{font-size:11.5px}
  .card--a .person{color:var(--card-white)}
  .card--b .person-name{color:var(--brand-blue)}
  .card--b .person-role{color:var(--ink-dark)}

  .tagline{position:absolute;left:0;right:0;top:214px;text-align:center;font-size:13px}
  .card--a .tagline{color:var(--card-white)}
  .card--b .tagline{color:var(--brand-blue)}
  .tagline-rule{position:absolute;left:150px;right:150px;top:236px;height:1px}
  .card--a .tagline-rule{background:rgba(255,255,255,.6)}
  .card--b .tagline-rule{background:var(--brand-blue-pale)}

  .option-label{position:absolute;width:516px;text-align:center;font-family:"Cinzel",Georgia,serif;font-size:20px;letter-spacing:2px;color:var(--label-ink)}
  .option-label--front{top:442px}
  .option-label--back{top:795px;font-size:19px}
  .label-a{left:65px}
  .label-b{left:619px}
</style>
</head>
<body>

<section class="card card--front card--a">
  <svg class="card-bg" viewBox="0 0 516 372" preserveAspectRatio="none">
    <rect width="516" height="372" fill="var(--card-white)"/>
    <path d="M0,150 C120,115 230,150 340,100 C420,65 470,50 516,45 V372 H0 Z" fill="var(--brand-blue-light)"/>
    <path d="M0,165 C130,130 240,165 350,115 C430,80 475,68 516,64 V372 H0 Z" fill="var(--brand-blue)"/>
  </svg>
  <div class="skyline" role="img" aria-label="Faint city skyline illustration"></div>
  <div class="brand brand--front"><span class="brand-mark"></span>TownDailyo</div>
  <ul class="contacts">
    <li><svg class="icon" viewBox="0 0 12 12"><path d="M3 1h2l1 3-1.5 1a6 6 0 0 0 2.5 2.5L8 6l3 1v2a2 2 0 0 1-2 2A8 8 0 0 1 1 3a2 2 0 0 1 2-2z" fill="currentColor"/></svg>555-014-2270</li>
    <li><svg class="icon" viewBox="0 0 12 12"><rect x="1" y="2.5" width="10" height="7" rx="1" fill="none" stroke="currentColor"/><path d="M1 3l5 4 5-4" fill="none" stroke="currentColor"/></svg>marcus@towndailyo.example</li>
    <li><svg class="icon" viewBox="0 0 12 12"><circle cx="6" cy="6" r="5" fill="none" stroke="currentColor"/><path d="M1 6h10M6 1c2 2 2 8 0 10M6 1c-2 2-2 8 0 10" fill="none" stroke="currentColor"/></svg>www.towndailyo.example</li>
    <li><span class="social-box"></span>TOWNDAILYO</li>
    <li><span class="social-box"></span>TOWNDAILYO</li>
  </ul>
  <div class="person"><div class="person-name">Marcus Delwyn</div><div class="person-role">Creator + Director</div></div>
</section>

<section class="card card--front card--b">
  <svg class="card-bg" viewBox="0 0 516 372" preserveAspectRatio="none">
    <rect width="516" height="372" fill="var(--card-white)"/>
    <path d="M0,128 C120,98 230,132 340,90 C420,60 470,48 516,44 V60 C470,64 425,78 350,106 C240,148 130,114 0,146 Z" fill="var(--brand-blue)"/>
    <path d="M0,150 C130,120 240,154 352,112 C430,82 475,70 516,66 V74 C475,78 432,92 356,120 C242,162 132,130 0,160 Z" fill="var(--brand-blue-light)"/>
  </svg>
  <div class="skyline" role="img" aria-label="Faint city skyline illustration"></div>
  <div class="brand brand--front"><span class="brand-mark"></span>TownDailyo</div>
  <ul class="contacts">
    <li><svg class="icon" viewBox="0 0 12 12"><path d="M3 1h2l1 3-1.5 1a6 6 0 0 0 2.5 2.5L8 6l3 1v2a2 2 0 0 1-2 2A8 8 0 0 1 1 3a2 2 0 0 1 2-2z" fill="var(--brand-blue)"/></svg>555-014-2270</li>
    <li><svg class="icon" viewBox="0 0 12 12"><rect x="1" y="2.5" width="10" height="7" rx="1" fill="none" stroke="var(--brand-blue)"/><path d="M1 3l5 4 5-4" fill="none" stroke="var(--brand-blue)"/></svg>marcus@towndailyo.example</li>
    <li><svg class="icon" viewBox="0 0 12 12"><circle cx="6" cy="6" r="5" fill="none" stroke="var(--brand-blue)"/><path d="M1 6h10M6 1c2 2 2 8 0 10M6 1c-2 2-2 8 0 10" fill="none" stroke="var(--brand-blue)"/></svg>www.towndailyo.example</li>
    <li><span class="social-box"></span>TOWNDAILYO</li>
    <li><span class="social-box"></span>TOWNDAILYO</li>
  </ul>
  <div class="person"><div class="person-name">Marcus Delwyn</div><div class="person-role">Creator + Director</div></div>
</section>

<div class="option-label option-label--front label-a">Business Card Option A</div>
<div class="option-label option-label--front label-b">Business Card Option B</div>

<section class="card card--back card--a">
  <svg class="card-bg" viewBox="0 0 516 300" preserveAspectRatio="none"><rect width="516" height="300" fill="var(--brand-blue)"/></svg>
  <div class="brand brand--back"><span class="brand-mark size-lg"></span>TownDailyo</div>
  <div class="tagline">Discover fresh corners of your town, daily</div>
  <div class="tagline-rule"></div>
</section>

<section class="card card--back card--b">
  <svg class="card-bg" viewBox="0 0 516 300" preserveAspectRatio="none"><rect width="516" height="300" fill="var(--card-white)"/></svg>
  <div class="brand brand--back"><span class="brand-mark size-lg"></span>TownDailyo</div>
  <div class="tagline">Discover fresh corners of your town, daily</div>
  <div class="tagline-rule"></div>
</section>

<div class="option-label option-label--back label-a">Business Card Back</div>
<div class="option-label option-label--back label-b">Business Card Back</div>

</body>
</html>
```